Barrister in Western Australia needs a fully custom logo, stationery and fonts

Barrister based in Western Australia seeking a fully custom logo, electronic and hardcopy stationery set (including email signature, document headers and footers for use with retainer agreement, invoices, letters of advice etc), custom fonts and business card design. Certain non-optional wording regarding liability limitation has to appear on documents (wording will be supplied but is on the uploaded examples). Have used this platform previously and have outgrown the previous design - samples of which are attached. I live very close to, and spend a significant amount time when not working in or around, the ocean. Use of colours or designs representative of that would be appreciated. The final design should try and communicate strength (of representation), the ability to be flexible (for example, settlements) and the fact I make myself accessible to clients - all factors shown in water/ocean.

Target Market(s)

Legal services providers, solicitors

Industry/Entity Type

Legal

Font styles to use
Serif
Decorative

Requirements
Must have
• Certain insurance wording regarding limitation of liability. Progressive feel to the set including a custom font for use in Office 365. Logo or design that is progressive - can relate to the ocean, water or waves (representing an ability to be fluid, dynamic but inheerent strength)
Nice to have
• Colour
Should not have
• Traditional calligraphy or legal fonts or feel - should not contain any traditional legal industry designs such as pens, scales of justice etc.

```html
<!DOCTYPE html>
<html lang="en">
<head>
<meta charset="utf-8">
<title>Daniel R Ashcombe — Barrister Stationery</title>
<link rel="stylesheet" href="https://fonts.googleapis.com/css2?family=Work+Sans:ital,wght@0,100;0,400;0,500;0,700;0,800;1,400&family=Poppins:ital,wght@0,400;1,400&display=swap">
<style>
  :root {
    --ink: #2b3538;
    --ocean: #045a8d;
    --foam: #e3f0f4;
    --card: #f1f4f5;
    --page: #ffffff;
    --thin: #b7bcbe;
  }
  * { box-sizing: border-box; margin: 0; padding: 0; }
  html, body { width: 1200px; height: 1200px; overflow: hidden; background: var(--page); }
  body { position: relative; font-family: "Work Sans", sans-serif; color: var(--ink); }

  .letterhead {
    position: absolute; left: 60px; top: 114px; width: 688px; height: 975px;
    background: var(--page); box-shadow: 0 0 6px rgba(0,0,0,.25); overflow: hidden;
  }
  .letterhead__wash {
    position: absolute; left: 0; top: 390px; width: 688px; height: 600px;
    background: radial-gradient(ellipse at 85% 40%, var(--foam) 0%, rgba(227,240,244,.75) 45%, rgba(227,240,244,0) 75%);
  }
  .brand { position: absolute; text-align: center; }
  .brand__mark { display: block; margin: 0 auto; border-radius: 50%; background: var(--ocean); }
  .brand__name { font-weight: 800; letter-spacing: .01em; white-space: nowrap; line-height: 1; }
  .brand__role { font-weight: 500; white-space: nowrap; line-height: 1; }

  .brand--small { left: 40px; top: 28px; width: 208px; }
  .brand--small .brand__mark { width: 30px; height: 30px; margin-bottom: 24px; }
  .brand--small .brand__name { font-size: 21px; }
  .brand--small .brand__role { font-size: 10px; letter-spacing: .62em; margin-top: 6px; padding-left: .62em; }

  .brand--hero { left: 0; top: 356px; width: 688px; }
  .brand--hero .brand__mark { width: 70px; height: 70px; margin-bottom: 66px; }
  .brand--hero .brand__name { font-size: 60px; }
  .brand--hero .brand__role { font-size: 27px; letter-spacing: .9em; margin-top: 20px; padding-left: .9em; }

  .contact { position: absolute; left: 61px; top: 805px; font-family: "Poppins", sans-serif; }
  .contact__rule { width: 115px; height: 2px; background: var(--ocean); margin-bottom: 12px; }
  .contact__line { font-size: 10.5px; line-height: 13px; }
  .contact__line b { font-weight: 400; display: inline-block; width: 15px; }
  .disclaimer {
    position: absolute; left: 61px; top: 877px; width: 370px;
    font-family: "Poppins", sans-serif; font-style: italic; font-size: 9.3px; line-height: 11.2px;
  }
  .letterhead__band { position: absolute; left: 0; bottom: 0; width: 688px; height: 23px; background: var(--ocean); }

  .card {
    position: absolute; left: 699px; top: 89px; width: 473px; height: 272px;
    background: var(--card); box-shadow: 0 0 6px rgba(0,0,0,.22);
  }
  .brand--card { left: 0; top: 28px; width: 473px; }
  .brand--card .brand__mark { width: 52px; height: 52px; margin-bottom: 62px; }
  .brand--card .brand__name { font-size: 32px; }
  .brand--card .brand__role { font-size: 16px; letter-spacing: .62em; margin-top: 10px; padding-left: .62em; }
  .card__notice {
    position: absolute; left: 0; top: 231px; width: 473px; text-align: center;
    font-family: "Poppins", sans-serif; font-size: 8.6px;
  }

  .specimens { position: absolute; left: 782px; top: 382px; width: 340px; }
  .specimen { margin-bottom: 18px; }
  .specimen__label { font-size: 19px; font-weight: 400; line-height: 22px; letter-spacing: .02em; }
  .specimen__text { font-size: 16.6px; line-height: 20.1px; letter-spacing: .01em; }
  .specimen--thin .specimen__text { font-weight: 100; color: var(--thin); }
  .specimen--bold .specimen__text { font-weight: 700; }
  .specimen--italic .specimen__text { font-style: italic; }
</style>
</head>
<body>
  <section class="letterhead">
    <div class="letterhead__wash" role="img" aria-label="Large faint wave motif in pale sea blue"></div>

    <div class="brand brand--small">
      <span class="brand__mark"></span>
      <div class="brand__name">Daniel R Ashcombe</div>
      <div class="brand__role">BARRISTER</div>
    </div>

    <div class="brand brand--hero">
      <span class="brand__mark"></span>
      <div class="brand__name">Daniel R Ashcombe</div>
      <div class="brand__role">BARRISTER</div>
    </div>

    <div class="contact">
      <div class="contact__rule"></div>
      <p class="contact__line"><b>m.</b>+61 (0) 400 555 018</p>
      <p class="contact__line"><b>t.</b>+61 8 5550 0192</p>
      <p class="contact__line"><b>a.</b>Level 9, 140 Harbour Parade, Perth, WA,</p>
    </div>

    <p class="disclaimer">Disclaimer. Liability limited by a scheme approved under Professional Standards Legislation. This email (including any attachments) is confidential and may be privileged. It may be read, copied and used only by the intended recipient. If you have received it in error, please contact the sender immediately by return email. Please then delete both emails and do</p>

    <div class="letterhead__band"></div>
  </section>

  <section class="card">
    <div class="brand brand--card">
      <span class="brand__mark"></span>
      <div class="brand__name">Daniel R Ashcombe</div>
      <div class="brand__role">BARRISTER</div>
    </div>
    <p class="card__notice">Liability limited by a scheme approved under Professional Standards Legislation.</p>
  </section>

  <section class="specimens">
    <div class="specimen specimen--thin">
      <h3 class="specimen__label">Font: Work Sans, Thin</h3>
      <p class="specimen__text">Lorem ipsum dolor sit amet, consectetur adipiscing elit, sed do eiusmod tempor incididunt ut labore et dolore magna aliqua. Quis ipsum suspendisse ultrices gravida. Risus commodo viverra maecenas accumsan lacus vel facilisis.</p>
    </div>
    <div class="specimen specimen--regular">
      <h3 class="specimen__label">Font: Work Sans Regular</h3>
      <p class="specimen__text">Lorem ipsum dolor sit amet, consectetur adipiscing elit, sed do eiusmod tempor incididunt ut labore et dolore magna aliqua. Quis ipsum suspendisse ultrices gravida. Risus commodo viverra maecenas accumsan lacus vel facilisis.</p>
    </div>
    <div class="specimen specimen--bold">
      <h3 class="specimen__label">Font: Work Sans, Bold</h3>
      <p class="specimen__text">Lorem ipsum dolor sit amet, consectetur adipiscing elit, sed do eiusmod tempor incididunt ut labore et dolore magna aliqua. Quis ipsum suspendisse ultrices gravida. Risus commodo viverra maecenas accumsan lacus vel facilisis.</p>
    </div>
    <div class="specimen specimen--italic">
      <h3 class="specimen__label">Font: Work Sans, Italic</h3>
      <p class="specimen__text">Lorem ipsum dolor sit amet, consectetur adipiscing elit, sed do eiusmod tempor incididunt ut labore et dolore magna aliqua. Quis ipsum suspendisse ultrices gravida. Risus commodo viverra maecenas accumsan lacus vel facilisis.</p>
    </div>
  </section>
</body>
</html>
```